Feedback App to request feedback from colleagues

It’s a small web app to collect feedback from team members. This is the general screen flow but happy for variations to it.

Users logs into application and is able to see the feedback received till date from different colleagues.

At the top right are “Request feedback”, “Respond to Feedback”.

When the user clicks on Request Feedback, there are three options.
Adhoc Feedback
Mid Year Feedback
360 Feedback

Adhoc feedback will open a screen where I can search for colleagues to request feedback from (I can select more than one). There are three pre-defined question that can I edit if needed.

Mid year feedback: same process but questions cannot be edited

360 Feedback - just redirect to another website.

Respond to Feedback - see incoming request and the ability to provide feedback to questions received.

Send Feedback: select a colleague and send adhoc feedback.

Colours to be used are white and red only. Simple design, the app will be embedded in a portal so need for headers etc. think of a mobile view but no need for logo, header bar etc

Colour Codes:
Red: #E60000
White #FFFFFF
Grey: #333333 (Only use if needed e.g. borders, background etc)
Black: #000000

Only the above colours to be used

Number of Pages Required

1 page

Font styles to use
Sans Serif

Colors
EB3D1F
EC4F4E
F09395
F8D3D4
FCEDEE

Requirements
Must have
• Design screens for every page mentioned
Nice to have
• Clean design, use of images and icons
Should not have
• Cluttered design, header

```html
<!DOCTYPE html>
<html lang="en">
<head>
<meta charset="utf-8">
<title>Feedback App Screens</title>
<link href="https://fonts.googleapis.com/css2?family=Roboto:wght@400;500;700&display=swap" rel="stylesheet">
<style>
:root{
  --red:#eb3d1f;
  --red-soft:#ec4f4e;
  --pink-mid:#f09395;
  --pink-light:#f8d3d4;
  --pink-bg:#fcedee;
  --navy:#1b2640;
  --green:#35d59a;
  --green-dark:#166b4a;
  --blue:#7b93fa;
  --ink:#1a1a1a;
  --muted:#555;
  --line:#e2e2e2;
  --grey-bg:#f3f3f7;
  --white:#fff;
  --bar:#000;
}
*{box-sizing:border-box;margin:0;padding:0}
html,body{width:1200px;height:1090px;overflow:hidden;background:var(--white)}
body{font-family:'Roboto',sans-serif;color:var(--ink)}
.stage{position:absolute;left:0;top:0;width:2000px;height:1817px;transform:scale(.6);transform-origin:0 0}
.phone{position:absolute;width:368px;height:798px;overflow:hidden;background:var(--grey-bg);box-shadow:0 2px 8px rgba(0,0,0,.12)}
.phone.pink{background:var(--pink-bg)}
.phone.flat{box-shadow:none;background:linear-gradient(#f3f3f3 0,#f3f3f3 300px,#f7f7fa 300px)}
.status{height:18px;background:var(--bar);color:#fff;font-size:13px;display:flex;justify-content:flex-end;align-items:center;gap:5px;padding-right:10px}
.status svg{display:block}
.appbar{height:44px;background:var(--white);display:flex;align-items:center;position:relative;border-bottom:1px solid #eee}
.appbar .title{position:absolute;left:0;right:0;text-align:center;font-size:14px;font-weight:500}
.appbar .title.left{text-align:left;left:15px}
.appbar .back{position:absolute;left:14px;top:13px}
.appbar .action{position:absolute;right:14px;top:11px}
.art{position:absolute;border-radius:8px}
.card{position:absolute;left:14px;width:340px;background:var(--white);border-radius:6px;box-shadow:0 2px 10px rgba(0,0,0,.06)}
.btn{position:absolute;left:31px;width:306px;height:52px;border-radius:5px;color:#fff;font-size:18px;font-weight:500;letter-spacing:.5px;display:flex;align-items:center;justify-content:center}
.btn.wide{left:16px;width:338px}
.btn-navy{background:var(--navy)}
.btn-red{background:var(--red)}
.btn-green{background:var(--green)}
.btn-green-dark{background:var(--green-dark)}
.btn-blue{background:var(--blue)}
.btn-coral{background:var(--red-soft)}
.profile{position:absolute;left:14px;width:339px;height:72px;background:var(--white);display:flex;align-items:center;overflow:hidden}
.avatar{width:34px;height:34px;border-radius:50%;margin:0 17px 0 9px;flex:none}
.profile .name{font-size:15px;font-weight:500;line-height:18px}
.profile .sub{font-size:13px;color:var(--muted);margin-top:4px;white-space:nowrap}
.check{position:absolute;right:11px;top:15px;width:12px;height:12px;border:1px solid #ccc;border-radius:2px}
.check.on{border-color:var(--pink-mid)}
.qcard{position:absolute;left:14px;width:340px;height:93px;background:var(--white);display:flex;padding:12px 44px 0 7px}
.num{color:var(--red);font-size:21px;font-weight:500;margin-right:8px;line-height:22px}
.qtext{font-size:15px;line-height:24.5px;margin-top:-3px}
.edit{position:absolute;right:11px;top:12px;width:29px;height:28px;background:var(--green);border-radius:2px;display:flex;align-items:center;justify-content:center}
.label{position:absolute;left:17px;font-size:13.5px;font-weight:500}
.field{position:absolute;left:16px;width:307px;border:1px solid var(--line);border-radius:4px;font-size:12.5px;color:#999;padding:12px 15px;line-height:16px}
.acard{position:absolute;left:14px;width:340px;height:223px;background:var(--white);border-radius:6px;box-shadow:0 2px 10px rgba(0,0,0,.05)}
.acard .q{position:absolute;left:11px;top:25px;right:10px;display:flex}
.acard .q .num{font-size:18px;margin-right:7px;line-height:18px;flex:none}
.acard .q p{font-size:14px;font-weight:500;line-height:16.5px}
</style>
</head>
<body>
<div class="stage">

<section class="phone" style="left:132px;top:47px">
  <div class="status"><svg width="14" height="10" viewBox="0 0 14 10"><path d="M7 10 0 3a10 10 0 0 1 14 0z" fill="#fff"/></svg><svg width="10" height="10"><path d="M0 10h10V0z" fill="#fff"/></svg><svg width="6" height="11"><rect width="6" height="11" fill="#fff"/></svg>12:30</div>
  <div class="appbar"><span class="title left">Feedback</span>
    <svg class="action" width="18" height="18" viewBox="0 0 18 18"><path d="M5 4.5a6 6 0 1 0 8 0" fill="none" stroke="#eb3d1f" stroke-width="1.6"/><path d="M9 2v6" stroke="#eb3d1f" stroke-width="1.6"/></svg></div>
  <div class="art" role="img" aria-label="Illustration of two people beside a large red star with rating icons" style="left:70px;top:80px;width:230px;height:220px;background:radial-gradient(circle at 55% 50%,#f26a55 0,#f4a093 35%,#f3f3f7 70%)"></div>
  <div style="position:absolute;left:0;top:362px;width:368px;height:436px;background:#f5f5f9"></div>
  <div class="card" style="top:303px;height:200px"></div>
  <div class="btn btn-navy" style="top:336px">Request feedback</div>
  <div class="btn btn-red" style="top:419px">Respond to Feedback</div>
</section>

<section class="phone" style="left:591px;top:47px">
  <div class="status"><svg width="14" height="10" viewBox="0 0 14 10"><path d="M7 10 0 3a10 10 0 0 1 14 0z" fill="#fff"/></svg><svg width="10" height="10"><path d="M0 10h10V0z" fill="#fff"/></svg><svg width="6" height="11"><rect width="6" height="11" fill="#fff"/></svg>12:30</div>
  <div class="appbar"><svg class="back" width="18" height="16" viewBox="0 0 18 16"><path d="M17 8H2M8 2 2 8l6 6" fill="none" stroke="#111" stroke-width="1.8"/></svg><span class="title">Request Feedback</span></div>
  <div class="art" role="img" aria-label="Illustration of a person leaning on a tablet showing rating faces and stars" style="left:55px;top:80px;width:260px;height:205px;background:radial-gradient(circle at 50% 60%,#e86060 0,#f2b6b6 25%,#e6e6e6 55%,#f3f3f7 75%)"></div>
  <div style="position:absolute;left:0;top:362px;width:368px;height:436px;background:#f5f5f9"></div>
  <div class="card" style="top:311px;height:292px"></div>
  <div class="btn btn-green" style="top:345px">Adhoc Feedback</div>
  <div class="btn btn-blue" style="top:428px">Mid Year Feedback</div>
  <div class="btn btn-coral" style="top:511px">360 Feedback</div>
</section>

<section class="phone flat" style="left:1051px;top:47px">
  <div class="status"><svg width="14" height="10" viewBox="0 0 14 10"><path d="M7 10 0 3a10 10 0 0 1 14 0z" fill="#fff"/></svg><svg width="10" height="10"><path d="M0 10h10V0z" fill="#fff"/></svg><svg width="6" height="11"><rect width="6" height="11" fill="#fff"/></svg>12:30</div>
  <div class="appbar"><svg class="back" width="18" height="16" viewBox="0 0 18 16"><path d="M17 8H2M8 2 2 8l6 6" fill="none" stroke="#111" stroke-width="1.8"/></svg><span class="title">Request Feedback</span></div>
  <div class="art" role="img" aria-label="Illustration of a person leaning on a tablet showing rating faces and stars" style="left:55px;top:80px;width:260px;height:205px;background:radial-gradient(circle at 50% 60%,#e86060 0,#f2b6b6 25%,#e6e6e6 55%,#f3f3f3 75%)"></div>
  <div class="card" style="top:311px;height:292px"></div>
  <div class="btn btn-green-dark" style="top:345px">Adhoc Feedback</div>
  <svg style="position:absolute;left:296px;top:383px" width="16" height="22" viewBox="0 0 16 22"><path d="M5 1.5v12l-2.5-2.5c-1-1-2.5.3-1.5 1.5l5 7.5h8V11c0-1-1.5-1.5-2-.5 0-1-1.5-1.5-2-.5 0-1-1.5-1.5-2-.5V1.5c0-1-2-1-2 0z" fill="#fff" stroke="#111" stroke-width="1"/></svg>
  <div class="btn btn-blue" style="top:428px">Mid Year Feedback</div>
  <div class="btn btn-coral" style="top:511px">360 Feedback</div>
</section>

<section class="phone pink" style="left:1510px;top:47px">
  <div class="status"><svg width="14" height="10" viewBox="0 0 14 10"><path d="M7 10 0 3a10 10 0 0 1 14 0z" fill="#fff"/></svg><svg width="10" height="10"><path d="M0 10h10V0z" fill="#fff"/></svg><svg width="6" height="11"><rect width="6" height="11" fill="#fff"/></svg>12:30</div>
  <div class="appbar"><svg class="back" width="18" height="16" viewBox="0 0 18 16"><path d="M17 8H2M8 2 2 8l6 6" fill="none" stroke="#111" stroke-width="1.8"/></svg><span class="title">Select Profile</span></div>
  <div class="art" role="img" aria-label="Illustration of people around a phone showing rated profile cards" style="left:75px;top:73px;width:210px;height:152px;background:radial-gradient(ellipse at 50% 55%,#4f78c8 0,#9fbbe8 40%,#fcedee 75%)"></div>
  <div class="profile" style="top:250px"><div class="avatar" style="background:#bcd3f0"></div><div><div class="name">Clara Stone</div><div class="sub">Lorem Ipsum is simply dummy text</div></div><span class="check on"><svg width="10" height="10" viewBox="0 0 10 10"><path d="M2 5l2 2 4-4" fill="none" stroke="#eb3d1f" stroke-width="1.2"/></svg></span></div>
  <div class="profile" style="top:340px"><div class="avatar" style="background:#f4c04a"></div><div><div class="name">Sonia Marks</div><div class="sub">Lorem Ipsum is simply dummy text</div></div><span class="check on"><svg width="10" height="10" viewBox="0 0 10 10"><path d="M2 5l2 2 4-4" fill="none" stroke="#eb3d1f" stroke-width="1.2"/></svg></span></div>
  <div class="profile" style="top:434px;height:70px"><div class="avatar" style="background:#e84a4a"></div><div><div class="name">Tobias Crane</div><div class="sub">Lorem Ipsum is simply dummy text</div></div><span class="check on"><svg width="10" height="10" viewBox="0 0 10 10"><path d="M2 5l2 2 4-4" fill="none" stroke="#eb3d1f" stroke-width="1.2"/></svg></span></div>
  <div class="profile" style="top:524px;height:70px"><div class="avatar" style="background:#f6c940"></div><div><div class="name">Anika Dale</div><div class="sub">Lorem Ipsum is simply dummy text</div></div><span class="check"></span></div>
  <div class="profile" style="top:616px;height:47px;align-items:flex-start;padding-top:14px"><div class="avatar" style="background:#ee6a5a"></div><div><div class="name">Tim porter</div><div class="sub">Lorem Ipsum is simply dummy text</div></div><span class="check"></span></div>
  <div class="btn btn-red wide" style="top:711px;left:15px">Continue</div>
</section>

<section class="phone pink" style="left:132px;top:911px">
  <div class="status"><svg width="14" height="10" viewBox="0 0 14 10"><path d="M7 10 0 3a10 10 0 0 1 14 0z" fill="#fff"/></svg><svg width="10" height="10"><path d="M0 10h10V0z" fill="#fff"/></svg><svg width="6" height="11"><rect width="6" height="11" fill="#fff"/></svg>12:30</div>
  <div class="appbar"><svg class="back" width="18" height="16" viewBox="0 0 18 16"><path d="M17 8H2M8 2 2 8l6 6" fill="none" stroke="#111" stroke-width="1.8"/></svg><span class="title">Questions</span></div>
  <div class="art" role="img" aria-label="Illustration of a person leaning on a large red question mark" style="left:100px;top:70px;width:200px;height:190px;background:radial-gradient(ellipse at 45% 55%,#c0303a 0,#e58a8e 35%,#fcedee 72%)"></div>
  <div class="qcard" style="top:279px"><span class="num">01</span><p class="qtext">Lorem Ipsum is simply dummy text of the printing and typesetting industry. Lorem Ipsum has been ?</p><span class="edit"><svg width="13" height="13" viewBox="0 0 13 13"><path d="M6 2H1.5v9.5H11V7M5 8l.5-2.5L11 0l2 2-5.5 5.5z" fill="none" stroke="#fff" stroke-width="1.2"/></svg></span></div>
  <div class="qcard" style="top:392px"><span class="num">02</span><p class="qtext">Lorem Ipsum is simply dummy text of the printing and typesetting industry. Lorem Ipsum has been ?</p><span class="edit"><svg width="13" height="13" viewBox="0 0 13 13"><path d="M6 2H1.5v9.5H11V7M5 8l.5-2.5L11 0l2 2-5.5 5.5z" fill="none" stroke="#fff" stroke-width="1.2"/></svg></span></div>
  <div class="qcard" style="top:507px"><span class="num">03</span><p class="qtext">Lorem Ipsum is simply dummy text of the printing and typesetting industry. Lorem Ipsum has been ?</p><span class="edit"><svg width="13" height="13" viewBox="0 0 13 13"><path d="M6 2H1.5v9.5H11V7M5 8l.5-2.5L11 0l2 2-5.5 5.5z" fill="none" stroke="#fff" stroke-width="1.2"/></svg></span></div>
  <div class="btn btn-red wide" style="top:711px">Submit</div>
</section>

<section class="phone pink" style="left:591px;top:911px">
  <div class="status"><svg width="14" height="10" viewBox="0 0 14 10"><path d="M7 10 0 3a10 10 0 0 1 14 0z" fill="#fff"/></svg><svg width="10" height="10"><path d="M0 10h10V0z" fill="#fff"/></svg><svg width="6" height="11"><rect width="6" height="11" fill="#fff"/></svg>12:30</div>
  <div class="appbar"><svg class="back" width="18" height="16" viewBox="0 0 18 16"><path d="M17 8H2M8 2 2 8l6 6" fill="none" stroke="#111" stroke-width="1.8"/></svg><span class="title">Questions Edit</span></div>
  <div class="art" role="img" aria-label="Illustration of a person leaning on a large red question mark" style="left:100px;top:70px;width:200px;height:190px;background:radial-gradient(ellipse at 45% 55%,#c0303a 0,#e58a8e 35%,#fcedee 72%)"></div>
  <div class="card" style="top:285px;height:291px">
    <span class="label" style="top:27px">Question&nbsp; No.</span>
    <div class="field" style="top:52px;height:53px;padding-top:18px">01</div>
    <span class="label" style="top:123px">Question</span>
    <div class="field" style="top:150px;height:92px;padding-top:21px">Lorem Ipsum is simply dummy text of the printing and typesetting industry. Lorem Ipsum has been ?</div>
  </div>
  <div class="btn btn-red wide" style="top:711px">Update</div>
</section>

<section class="phone pink" style="left:1051px;top:911px">
  <div class="status"><svg width="14" height="10" viewBox="0 0 14 10"><path d="M7 10 0 3a10 10 0 0 1 14 0z" fill="#fff"/></svg><svg width="10" height="10"><path d="M0 10h10V0z" fill="#fff"/></svg><svg width="6" height="11"><rect width="6" height="11" fill="#fff"/></svg>12:30</div>
  <div class="appbar"><svg class="back" width="18" height="16" viewBox="0 0 18 16"><path d="M17 8H2M8 2 2 8l6 6" fill="none" stroke="#111" stroke-width="1.8"/></svg><span class="title">Answer</span>
    <svg class="action" width="20" height="22" viewBox="0 0 20 22"><path d="M4 15V9a6 6 0 0 1 12 0v6l2 2H2zM8 19a2 2 0 0 0 4 0M10 1v2" fill="none" stroke="#111" stroke-width="1.5"/></svg></div>
  <div class="acard" style="top:88px"><div class="q"><span class="num">01</span><p>Lorem Ipsum is simply dummy text of the printing and typesetting industry. Lorem Ipsum has been ?</p></div><span class="label" style="top:90px">Answer</span><div class="field" style="top:112px;height:92px">Enter Your Answer</div></div>
  <div class="acard" style="top:341px"><div class="q"><span class="num">02</span><p>Lorem Ipsum is simply dummy text of the printing and typesetting industry. Lorem Ipsum has been ?</p></div><span class="label" style="top:90px">Answer</span><div class="field" style="top:112px;height:92px">Enter Your Answer</div></div>
  <div style="position:absolute;left:0;top:587px;width:368px;height:99px;overflow:hidden"><div class="acard" style="top:0"><div class="q"><span class="num">03</span><p>Lorem Ipsum is simply dummy text of the printing and typesetting industry. Lorem Ipsum has been ?</p></div><span class="label" style="top:90px">Answer</span></div></div>
  <div class="btn btn-red wide" style="top:711px">Submit</div>
</section>

</div>
</body>
</html>
```